Website Design For Atelier Nine Design Group

Create a sophisticated website that denotes high-end luxury. We would like to keep the copy minimalist and elegantly understated while communicating only the most essential information. While creating an air of exclusivity.
We would like 3-4 Tab Wesbite
Home:
• Feature a design project front and centre, along with a short
introduction about who we are and what we do.

We can put a Call To Action at the end of the introduction inviting readers to learn more on our About page.
About:
• This page should provide more detail on our background, past
achievements, history of the company, and anything you'd like to
highlight.
• We should also provide details on our services, aesthetic, process, etc.
Team:
• introduce the team, possibly with short descriptions for each
team member. Total Team Members 7
Residential
• The portfolio page can be a grid of images along with titles for
each project.
• Clicking on each image should take you to a separate page for that
project where readers can find more details

Commercial
The portfolio page can be a grid of images along with titles for
each project.

Contact Us:

example website:
https://www.morvexinteriors.example/

Target Market(s)

High end luxury clientele

Industry/Entity Type

Interior Design

Number of Pages Required

4 page

Font styles to use
Sans Serif

Requirements
Must have
• Company logo, color scheme and name: Atelier Nine Design Group

```html
<!DOCTYPE html>
<html lang="en">
<head>
<meta charset="utf-8">
<title>Atelier Nine Design Group</title>
<link href="https://fonts.googleapis.com/css2?family=Rajdhani:wght@600;700&family=Heebo:wght@400;500;600&display=swap" rel="stylesheet">
<style>
:root{
  --navy:#1b2152;
  --navy-deep:#141838;
  --gold:#a57f2c;
  --ink:#3d4150;
  --muted:#6b6f7c;
  --pale:#f2f3f6;
  --white:#ffffff;
  --line:#9a9da8;
  --tint:#dfe1ea;
}
*{margin:0;padding:0;box-sizing:border-box}
html,body{width:1200px;height:4773px;overflow:hidden}
body{position:relative;font-family:"Heebo",sans-serif;color:var(--ink);background:var(--white)}
.abs{position:absolute}
.heading{font-family:"Rajdhani",sans-serif;font-weight:700;color:var(--navy);letter-spacing:.5px}
.section-title{left:0;width:1200px;text-align:center;font-size:42px;line-height:1}
.rule{width:66px;height:3px;background:var(--gold);left:567px}
.btn{display:flex;align-items:center;justify-content:center;border:2px solid var(--gold);color:var(--gold);font-family:"Heebo",sans-serif;font-weight:600;font-size:14px;letter-spacing:.5px;text-transform:uppercase}
.copy{font-size:13px;line-height:27px;color:var(--muted)}
.topbar{font-size:14px;color:var(--ink);top:22px;display:flex;align-items:center;gap:8px}
.nav{top:80px;display:flex;gap:36px;font-size:14px;color:var(--ink);text-transform:uppercase}
.nav .active{color:var(--gold)}
.brand{left:450px;width:300px;top:22px;text-align:center}
.brand-mark{display:inline-block;width:16px;height:16px;background:var(--navy)}
.brand-name{display:block;font-family:"Rajdhani",sans-serif;font-weight:700;font-size:26px;color:var(--navy);letter-spacing:3px;line-height:1.2;margin-top:4px}
.hero{top:118px;left:0;width:1200px;height:644px;background:linear-gradient(180deg,#3a4250 0%,#2f3744 55%,#6b4a30 78%,#7b7d80 100%)}
.hero-title{top:208px;font-size:44px;color:var(--white)}
.hero-copy{top:272px;left:290px;width:620px;text-align:center;color:#e6e7ea;font-size:14px;line-height:29px}
.hero-btn{left:477px;top:387px;width:246px;height:58px;border:2px solid var(--white);color:var(--white);display:flex;align-items:center;justify-content:center;font-weight:600;font-size:14px}
.welcome{top:762px;left:0;width:1200px;height:465px;background:var(--pale)}
.photo{background:linear-gradient(160deg,#4a4d50,#2b2d2f 60%,#6c6e6c)}
.frame{border:1.5px solid var(--gold)}
.service-title{font-size:34px}
.accent-block{background:linear-gradient(135deg,var(--tint),rgba(223,225,234,.35))}
.team{top:2555px;left:0;width:1200px;height:580px;background:var(--pale)}
.member{width:230px;text-align:center}
.portrait{width:216px;height:216px;border-radius:50%;margin:0 auto;border:5px solid var(--white);box-shadow:0 4px 10px rgba(0,0,0,.18)}
.member-name{margin-top:12px;font-weight:600;font-size:15px;color:var(--ink)}
.member-role{font-size:12px;color:var(--muted);margin-top:2px}
.field-label{font-size:14px;color:var(--muted)}
.field-line{height:1.5px;background:var(--line)}
.project{width:222px;height:273px;top:4024px}
.footer{top:4315px;left:0;width:1200px;height:458px;background:var(--navy-deep);color:#d8dae3}
.foot-h{font-family:"Heebo",sans-serif;font-weight:500;font-size:16px;color:var(--white);letter-spacing:.5px}
.foot-list{font-size:14px;line-height:31px;color:#d8dae3;list-style:none}
.foot-list svg{vertical-align:-2px;margin-right:6px}
.foot-bar{width:36px;height:2px;background:var(--white);margin-top:8px}
.social{width:44px;height:44px;border:1.5px solid var(--white);border-radius:50%;display:flex;align-items:center;justify-content:center}
</style>
</head>
<body>

<header>
  <div class="abs topbar" style="left:111px">
    <svg width="12" height="12" viewBox="0 0 24 24"><path fill="#a57f2c" d="M6.6 10.8a15 15 0 0 0 6.6 6.6l2.2-2.2c.3-.3.7-.4 1-.2 1.1.4 2.3.6 3.6.6.6 0 1 .4 1 1V20c0 .6-.4 1-1 1A17 17 0 0 1 3 4c0-.6.4-1 1-1h3.5c.6 0 1 .4 1 1 0 1.3.2 2.5.6 3.6.1.3 0 .7-.2 1z"/></svg>
    <span>CALL NOW - +1 555 014 2090</span>
  </div>
  <div class="abs topbar" style="right:115px">
    <svg width="14" height="11" viewBox="0 0 24 18"><rect width="24" height="18" rx="2" fill="#a57f2c"/><path d="M1 2l11 8 11-8" stroke="#fff" stroke-width="2" fill="none"/></svg>
    <span>hello@ateliernine.example</span>
  </div>
  <div class="abs brand">
    <span class="brand-mark"></span>
    <span class="brand-name">ATELIER NINE</span>
  </div>
  <nav class="abs nav" style="left:111px">
    <span class="active">Home</span><span>About</span><span>Team</span><span>Residential</span>
  </nav>
  <nav class="abs nav" style="left:733px;gap:38px">
    <span>Commercial</span><span>Contact Us</span>
    <span style="display:flex;align-items:center;gap:6px"><svg width="14" height="14" viewBox="0 0 24 24"><circle cx="12" cy="12" r="10" fill="none" stroke="#3d4150" stroke-width="2"/><circle cx="12" cy="10" r="3.5" fill="#3d4150"/><path d="M5.5 19a8 8 0 0 1 13 0" fill="#3d4150"/></svg>Login</span>
    <svg width="14" height="14" viewBox="0 0 24 24" style="margin-left:-14px"><circle cx="10" cy="10" r="6.5" fill="none" stroke="#1b2152" stroke-width="3"/><path d="M15 15l6 6" stroke="#1b2152" stroke-width="3"/></svg>
  </nav>
</header>

<section>
  <div class="abs hero" role="img" aria-label="Living room with a tan leather sectional sofa, table lamp and potted plants against a dark slate wall"></div>
  <h1 class="abs heading section-title hero-title">ATELIER NINE DESIGN GROUP</h1>
  <p class="abs hero-copy">Lorem ipsum dolor sit amet, consectetur adipiscing elit, sed do eiusmod tempor incididunt ut labore et dolore magna aliqua. Ut enim ad minim veniam, quis nostrud exercitation ullamco laboris nisi ut aliquip</p>
  <div class="abs hero-btn">GET STARTED</div>
  <svg class="abs" style="left:575px;top:682px" width="50" height="50" viewBox="0 0 50 50"><circle cx="25" cy="25" r="23" fill="none" stroke="#fff" stroke-width="2"/><path d="M16 21l9 9 9-9" fill="none" stroke="#fff" stroke-width="2"/></svg>
</section>

<section>
  <div class="abs welcome"></div>
  <h2 class="abs heading section-title" style="top:848px;font-size:36px">WELCOME TO ATELIER NINE DESIGN GROUP</h2>
  <div class="abs rule" style="top:905px"></div>
  <p class="abs copy" style="left:118px;width:964px;top:932px;text-align:center;font-size:13px;line-height:28.5px">Lorem ipsum dolor sit amet, consectetur adipiscing elit, sed do eiusmod tempor incididunt ut labore et dolore magna aliqua. Ut enim ad minim veniam, quis nostrud exercitation ullamco laboris nisi ut aliquip ex ea commodo consequat. Duis aute irure dolor in reprehenderit in voluptate velit esse cillum dolore eu fugiat nulla pariatur. Excepteur sint occaecat cupidatat non proident, sunt in culpa qui officia deserunt mollit anim id est laborum Lorem ipsum dolor sit amet, consectetur adipiscing elit, sed do eiusmod tempor incididunt ut labore et dolore magna aliqua. Ut enim ad minim veniam, quis nostrud exercitation ullamco laboris nisi ut aliquip ex ea commodo consequat. Duis aute irure dolor in reprehenderit in voluptate velit esse cillum</p>
  <div class="abs btn" style="left:477px;top:1095px;width:246px;height:57px">Read More</div>
</section>

<section>
  <div class="abs accent-block" style="left:1015px;top:1228px;width:185px;height:92px" role="img" aria-label="Decorative accent area"></div>
  <div class="abs accent-block" style="left:0;top:2463px;width:185px;height:92px" role="img" aria-label="Decorative accent area"></div>

  <h2 class="abs heading section-title" style="top:1300px">WHAT WE DO</h2>
  <div class="abs rule" style="top:1359px"></div>

  <div class="abs frame" style="left:93px;top:1448px;width:457px;height:495px"></div>
  <div class="abs photo" style="left:111px;top:1424px;width:456px;height:502px;box-shadow:0 6px 16px rgba(0,0,0,.2)" role="img" aria-label="Residential interior with dark shelving, ceramic vases and an upholstered armchair"></div>
  <h3 class="abs heading service-title" style="left:626px;top:1550px">Residential</h3>
  <p class="abs copy" style="left:626px;top:1604px;width:470px">Lorem ipsum dolor sit amet, consectetur adipiscing elit, sed do eiusmod tempor incididunt ut labore et dolore magna aliqua. Ut enim veniam, quis nostrud exercitation ullamco laboris nisi ut aliquip ex ea commodo consequat. Duis aute irure dolor in reprehenderit in voluptate velit</p>
  <div class="abs btn" style="left:626px;top:1735px;width:246px;height:56px">Read More</div>

  <h3 class="abs heading service-title" style="left:110px;top:2099px">Commercial</h3>
  <p class="abs copy" style="left:110px;top:2153px;width:470px">Lorem ipsum dolor sit amet, consectetur adipiscing elit, sed do eiusmod tempor incididunt ut labore et dolore magna aliqua. Ut enim veniam, quis nostrud exercitation ullamco laboris nisi ut aliquip ex ea commodo consequat. Duis aute irure dolor in reprehenderit in voluptate velit</p>
  <div class="abs btn" style="left:110px;top:2283px;width:247px;height:56px">Read More</div>
  <div class="abs frame" style="left:652px;top:1987px;width:454px;height:504px"></div>
  <div class="abs" style="left:633px;top:1972px;width:454px;height:500px;background:linear-gradient(180deg,#d6d3d0 0%,#bdb9b6 45%,#8a3b2e 66%,#4c4d52 100%);box-shadow:0 6px 16px rgba(0,0,0,.2)" role="img" aria-label="Open-plan office with arched windows, red lounge sofa and orange chairs at long desks"></div>
</section>

<section>
  <div class="abs team"></div>
  <h2 class="abs heading section-title" style="top:2625px">TEAM</h2>
  <div class="abs rule" style="top:2682px"></div>

  <div class="abs member" style="left:104px;top:2735px">
    <div class="portrait" style="background:linear-gradient(150deg,#d9d6d1,#8c8782)" role="img" aria-label="Portrait of a team member in an office"></div>
    <div class="member-name">Mara Ellison</div><div class="member-role">Lorem ipsum</div>
  </div>
  <div class="abs member" style="left:357px;top:2735px">
    <div class="portrait" style="background:#2c2f3a;display:flex;align-items:center;justify-content:center" role="img" aria-label="Team member portrait with description overlay">
      <p style="color:#fff;font-size:12px;line-height:24px;width:160px;text-align:center">Lorem ipsum dolor sit amet, consectetur adipiscing elit, sed do eiusmod tempor incididunt ut labore et dolore magna aliqua. Ut enim ad minim veniam,</p>
    </div>
    <div class="member-name">Mara Ellison</div><div class="member-role">Lorem ipsum</div>
  </div>
  <div class="abs member" style="left:611px;top:2735px">
    <div class="portrait" style="background:linear-gradient(150deg,#e8e6e2,#c9a06a)" role="img" aria-label="Portrait of a team member at a design desk"></div>
    <div class="member-name">Mara Ellison</div><div class="member-role">Lorem ipsum</div>
  </div>
  <div class="abs member" style="left:865px;top:2735px">
    <div class="portrait" style="background:linear-gradient(150deg,#3c4a44,#c58f3a)" role="img" aria-label="Portrait of a team member in a mustard blazer"></div>
    <div class="member-name">Mara Ellison</div><div class="member-role">Lorem ipsum</div>
  </div>

  <svg class="abs" style="left:579px;top:3057px" width="42" height="12" aria-hidden="true">
    <circle cx="6" cy="6" r="4.5" fill="none" stroke="#a57f2c" stroke-width="1.5"/><circle cx="6" cy="6" r="2" fill="#a57f2c"/>
    <circle cx="21" cy="6" r="4.5" fill="none" stroke="#1b2152" stroke-width="1.5"/>
    <circle cx="36" cy="6" r="4.5" fill="none" stroke="#1b2152" stroke-width="1.5"/>
  </svg>
</section>

<section>
  <h2 class="abs heading section-title" style="top:3200px">CONTACT US</h2>
  <div class="abs rule" style="top:3257px"></div>
  <p class="abs copy" style="left:170px;width:860px;top:3281px;text-align:center">Lorem ipsum dolor sit amet, consectetur adipiscing elit, sed do eiusmod tempor incididunt ut labore et dolore magna aliqua. Ut enim ad minim veniam, quis nostrud exercitation ullamco laboris nisi ut aliquip ex ea commodo consequatLorem ipsum dolor sit amet, consectetur adipiscing elit, sed do eiusmod tempor incididunt ut labore et dolore magna aliqua</p>

  <span class="abs field-label" style="left:228px;top:3407px">Name</span>
  <div class="abs field-line" style="left:228px;top:3437px;width:350px"></div>
  <span class="abs field-label" style="left:624px;top:3407px">Email Address</span>
  <div class="abs field-line" style="left:624px;top:3437px;width:348px"></div>
  <span class="abs field-label" style="left:228px;top:3477px">Phone Number</span>
  <div class="abs field-line" style="left:228px;top:3508px;width:350px"></div>
  <span class="abs field-label" style="left:624px;top:3477px">Subject</span>
  <div class="abs field-line" style="left:624px;top:3508px;width:348px"></div>
  <span class="abs field-label" style="left:228px;top:3545px">Message</span>
  <div class="abs field-line" style="left:228px;top:3645px;width:740px"></div>
  <div class="abs btn" style="left:477px;top:3690px;width:246px;height:56px">Submit</div>
</section>

<section>
  <h2 class="abs heading section-title" style="top:3867px">OUR PROJECTS</h2>
  <div class="abs rule" style="top:3924px"></div>

  <div class="abs project" style="left:13px;background:linear-gradient(160deg,#4b5249,#2a2c2b 55%,#8d8a84)" role="img" aria-label="Residential project with dark shelving and armchair"></div>
  <div class="abs" style="left:246px;top:3965px;width:236px;height:332px;background:#2a2422;border:6px solid #fff;box-shadow:0 6px 18px rgba(0,0,0,.3);display:flex;align-items:center;justify-content:center" role="img" aria-label="Featured project with description overlay">
    <p style="color:#fff;font-size:12px;line-height:24px;width:196px;text-align:center">Lorem ipsum dolor sit amet, consectetur adipiscing elit, sed do eiusmod tempor incididunt ut labore et dolore magna aliqua Lorem ipsum adipiscing elit, sed do eiusmod tempor incididunt ut labore et dolore magna aliqua</p>
  </div>
  <div class="abs project" style="left:491px;background:linear-gradient(160deg,#4e5a52,#d9d4cc 60%,#a69a8a)" role="img" aria-label="Bedroom project with striped curtains"></div>
  <div class="abs project" style="left:730px;background:linear-gradient(160deg,#6a6c6e,#b9b7b3 55%,#e7e6e3)" role="img" aria-label="Marble bathroom with freestanding tub"></div>
  <div class="abs project" style="left:969px;background:linear-gradient(160deg,#3b2e26,#8a6a4d 55%,#c7b49a)" role="img" aria-label="Industrial loft interior with wooden partitions"></div>

  <svg class="abs" style="left:24px;top:4145px" width="44" height="44" aria-hidden="true"><circle cx="22" cy="22" r="21" fill="#fff"/><path d="M25 15l-7 7 7 7" fill="none" stroke="#1b2152" stroke-width="2"/></svg>
  <svg class="abs" style="left:1139px;top:4145px" width="44" height="44" aria-hidden="true"><circle cx="22" cy="22" r="21" fill="#fff"/><path d="M19 15l7 7-7 7" fill="none" stroke="#1b2152" stroke-width="2"/></svg>
</section>

<footer>
  <div class="abs footer"></div>
  <h4 class="abs heading" style="left:111px;top:4404px;font-size:24px;color:#fff">ABOUT US</h4>
  <p class="abs" style="left:111px;top:4450px;width:290px;font-size:12px;line-height:24px;color:#d8dae3">Lorem ipsum dolor sit amet, consectetur adipiscing elit, sed do eiusmod tempor incididunt ut labore et dolore magna aliqua</p>
  <h5 class="abs foot-h" style="left:111px;top:4540px;font-size:15px">FOLLOW US</h5>
  <div class="abs social" style="left:111px;top:4584px" aria-label="Share">
    <svg width="16" height="16" viewBox="0 0 24 24"><circle cx="18" cy="5" r="3" fill="#fff"/><circle cx="6" cy="12" r="3" fill="#fff"/><circle cx="18" cy="19" r="3" fill="#fff"/><path d="M8.5 10.5l7-4M8.5 13.5l7 4" stroke="#fff" stroke-width="2"/></svg>
  </div>
  <div class="abs social" style="left:164px;top:4584px" aria-label="Message">
    <svg width="16" height="16" viewBox="0 0 24 24"><path d="M3 4h18v12H9l-5 4v-4H3z" fill="none" stroke="#fff" stroke-width="2" stroke-linejoin="round"/></svg>
  </div>
  <div class="abs social" style="left:217px;top:4584px" aria-label="Website">
    <svg width="16" height="16" viewBox="0 0 24 24"><circle cx="12" cy="12" r="9" fill="none" stroke="#fff" stroke-width="2"/><path d="M3 12h18M12 3c3 3 3 15 0 18M12 3c-3 3-3 15 0 18" fill="none" stroke="#fff" stroke-width="1.6"/></svg>
  </div>

  <div class="abs" style="left:459px;top:4385px;width:1px;height:273px;background:#d8dae3"></div>

  <div class="abs" style="left:543px;top:4403px">
    <div class="foot-h">CONTACT US</div><div class="foot-bar"></div>
    <ul class="foot-list" style="margin-top:6px;width:240px;line-height:28px">
      <li><svg width="12" height="12" viewBox="0 0 24 24"><path fill="#fff" d="M6.6 10.8a15 15 0 0 0 6.6 6.6l2.2-2.2c.3-.3.7-.4 1-.2 1.1.4 2.3.6 3.6.6.6 0 1 .4 1 1V20c0 .6-.4 1-1 1A17 17 0 0 1 3 4c0-.6.4-1 1-1h3.5c.6 0 1 .4 1 1 0 1.3.2 2.5.6 3.6.1.3 0 .7-.2 1z"/></svg>+ 555 014 2090</li>
      <li style="margin-top:6px"><svg width="10" height="14" viewBox="0 0 10 14"><path d="M5 0a5 5 0 0 1 5 5c0 4-5 9-5 9S0 9 0 5a5 5 0 0 1 5-5z" fill="#fff"/><circle cx="5" cy="5" r="2" fill="#141838"/></svg>Lorem ipsum dolor sit amet, consectetur adipiscing elit,</li>
      <li style="margin-top:6px"><svg width="13" height="10" viewBox="0 0 24 18"><rect width="24" height="18" rx="2" fill="#fff"/><path d="M1 2l11 8 11-8" stroke="#141838" stroke-width="2" fill="none"/></svg>hello@ateliernine.example</li>
    </ul>
  </div>

  <div class="abs" style="left:815px;top:4403px">
    <div class="foot-h">LINKS</div><div class="foot-bar"></div>
    <ul class="foot-list" style="margin-top:4px"><li>Home</li><li>About</li><li>Team</li><li>Residential</li><li>Commercial</li><li>Contact</li></ul>
  </div>
  <div class="abs" style="left:961px;top:4403px">
    <div class="foot-h">USEFUL LINKS</div><div class="foot-bar"></div>
    <ul class="foot-list" style="margin-top:4px"><li>FAQ</li><li>Privacy Policy</li><li>Terms</li><li>Blog</li></ul>
  </div>

  <p class="abs" style="left:0;width:1200px;top:4724px;text-align:center;font-size:14px;color:#d8dae3">© 2022 ATELIER NINE DESIGN GROUP, All Rights Reserved</p>
</footer>

</body>
</html>
```